Playful Website Design Needed Pet Sitting and Dog Walking Business

Need a simple one page Web Design Built on WordPress.
Sections:

About Us
Services Provided
Costs
Contact Us
Intake Form (Questionnaire that goes to email)
See us in Action

Industry/Entity Type

Pet Sitting and Dog Walking

Number of Pages Required

1 page

Font styles to use
Other font styles liked:
• See the Business Card Font and use that.

Colors
EE7325
F08F49
F5BC92
FAE3D3
FDF4ED

Requirements
Must have
• See attached Logo Design, with Font's and Colors Use these as theme guide

```html
<!DOCTYPE html>
<html lang="en">
<head>
<meta charset="utf-8">
<title>Paw Pals Care — Pet Sitting and Dog Walking</title>
<link rel="stylesheet" href="https://fonts.googleapis.com/css2?family=Gochi+Hand&family=Nunito:wght@400;600;700;800;900&display=swap">
<style>
:root{
  --orange:#fe5c00;
  --orange-soft:#f6813f;
  --cream:#faf6d9;
  --yellow:#f2e66d;
  --yellow-text:#f4d85a;
  --gold:#f6c90e;
  --green:#7dbf3e;
  --ink:#2d2a26;
  --ink-soft:#3b3b3b;
  --mint:#ddeedb;
  --sage:#e3e4c5;
  --stripe:#fbd98a;
  --stripe-green:#dfe8c9;
  --white:#ffffff;
}
*{margin:0;padding:0;box-sizing:border-box}
html,body{width:1200px;height:3337px;overflow:hidden;background:var(--white)}
body{font-family:"Nunito",sans-serif;color:var(--ink)}
.page{position:relative;width:1200px;height:3337px;overflow:hidden}
.abs{position:absolute}
.hand{font-family:"Gochi Hand",cursive;font-weight:400}
.photo{position:absolute}

/* header */
.hero-bg{position:absolute;left:0;top:0}
.nav{position:absolute;top:22px;left:600px;display:flex;gap:20px;font-size:12px;color:#444}
.logo-disc{left:70px;top:48px;width:228px;height:228px;border-radius:50%;background:var(--white);display:flex;align-items:center;justify-content:center}
.logo-name{font-family:"Nunito",sans-serif;font-weight:800;font-size:27px;color:var(--green);text-align:center;line-height:1.05}
.hero-halo{left:171px;top:130px;width:388px;height:388px;border-radius:50%;background:var(--orange-soft)}
.hero-dog{left:279px;top:222px;width:220px;height:420px;border-radius:90px 90px 40px 40px;background:linear-gradient(180deg,#b07a4e 0%,#e9e3dc 45%,#f2eee9 100%)}
.target-mark{left:470px;top:170px;width:134px;height:134px;border-radius:50%;background:rgba(255,255,255,.35)}
.hero-title{left:632px;top:200px;width:420px;font-weight:800;font-size:52px;line-height:56px;color:var(--white)}
.wave-mark{height:12px;border-radius:6px}
.stripe-disc{border-radius:50%}
.stripe-warm{background:linear-gradient(135deg,#fde7b4 0%,#fbd98a 100%)}
.stripe-cool{background:linear-gradient(135deg,#eef3e2 0%,#dfe8c9 100%)}

/* about */
.about-band{left:0;top:577px;width:730px;height:593px;background:var(--cream)}
.about-photo{left:670px;top:686px;width:530px;height:484px;background:linear-gradient(160deg,#4c7a2c 0%,#7ea24d 45%,#b7b5a6 80%,#8e8a80 100%)}
.about-title{left:250px;top:752px;font-size:66px;color:var(--yellow-text)}
.about-lead{left:250px;top:838px;font-size:15.5px;font-weight:800;color:var(--ink)}
.about-copy{left:250px;top:868px;width:352px;font-size:14.6px;line-height:20.7px;color:var(--ink-soft)}

/* services */
.services-title{left:0;width:1200px;top:1222px;text-align:center;font-size:50px;color:var(--green)}
.services-sub{left:0;width:1200px;top:1279px;text-align:center;font-size:16.5px;color:var(--ink-soft)}
.service{position:absolute;top:1342px;width:186px;text-align:center}
.service-photo{width:186px;height:186px;border-radius:50%}
.service-name{margin-top:20px;font-size:14.5px;color:var(--ink-soft)}
.divider{left:209px;top:1644px;height:2px;background:var(--green)}

/* costs */
.costs-title{left:276px;top:1722px;font-size:66px;color:var(--orange)}
.costs-note{left:560px;top:1733px;width:390px;font-size:16px;line-height:24.5px;color:var(--ink-soft)}
.rate-line{left:0;width:1200px;top:1856px;text-align:center;font-size:38px;color:var(--ink)}
.rate-card{position:absolute;top:1925px;width:201px;height:162px;text-align:center;padding-top:24px}
.rate-card h3{font-family:"Gochi Hand",cursive;font-weight:400;font-size:21px;color:#4a4a3a}
.rate-card p{font-size:11.5px;line-height:23px;color:var(--ink-soft);margin-top:4px}
.rate-card hr{width:36px;margin:3px auto 6px;border:0;border-top:2px solid #9bc56a}
.rate-card .price{font-size:30px;font-weight:600;color:var(--ink)}
.rate-card .price span{font-size:15px;vertical-align:8px;margin-right:2px}
.card-weekday{left:389px;background:var(--mint)}
.card-nights{left:614px;background:var(--sage)}
.rate-foot{left:0;width:1228px;top:2118px;text-align:center;font-size:26px;color:var(--ink)}
.retriever{left:985px;top:1892px;width:188px;height:331px;border-radius:80px 80px 30px 30px;background:linear-gradient(180deg,#e8c894 0%,#f1dcb7 50%,#dcb67f 100%)}

/* contact */
.contact-band{left:0;top:2223px}
.contact-art{left:39px;top:2307px;width:350px;height:343px;border-radius:40px;background:linear-gradient(160deg,#ecebe6 0%,#f4d23c 55%,#c99a17 100%)}
.contact-title{left:609px;top:2300px;font-size:72px;color:#4a4532}
.contact-hours{left:616px;top:2410px;font-size:13.5px;line-height:19.5px;color:var(--ink)}
.contact-address{left:617px;top:2500px;font-size:13.5px;line-height:19.5px;color:var(--ink)}
.contact-address strong{display:block;margin-bottom:6px;font-weight:800}
.owner-photo{left:742px;top:2568px;width:236px;height:236px;border-radius:48px;transform:rotate(-8deg);background:linear-gradient(160deg,#8aa0b8 0%,#4d6a8c 50%,#c79a60 100%)}
.corgi-photo{left:998px;top:2490px;width:250px;height:282px;border-radius:56px;transform:rotate(-12deg);border:6px solid var(--gold);background:linear-gradient(160deg,#d8b48a 0%,#c98a4f 50%,#e8d2b0 100%)}

/* conversation */
.talk-title{left:242px;top:2770px;font-size:64px;line-height:58px;color:var(--yellow-text)}
.talk-copy{left:245px;top:2958px;width:310px;font-size:13px;line-height:19px;color:var(--ink-soft)}
.pups-photo{left:0;top:2870px;width:320px;height:376px;background:linear-gradient(90deg,#b5c79a 0%,#d9c7a3 45%,rgba(255,255,255,0) 100%)}
.field{position:absolute;border-bottom:1.5px solid var(--ink);font-size:10.5px;font-weight:600;color:var(--ink);padding-bottom:10px}
.submit{left:605px;top:3104px;width:149px;height:28px;border-radius:5px;background:#000;color:var(--white);font-size:10.5px;font-weight:700;line-height:28px;padding-left:28px}

/* footer */
.footer-bg{left:0;top:3220px}
.copyright{left:0;width:1200px;top:3282px;text-align:center;font-size:12px;font-weight:700;color:var(--white)}
</style>
</head>
<body>
<div class="page">

  <!-- header -->
  <svg class="hero-bg" width="1200" height="640" viewBox="0 0 1200 640" aria-hidden="true">
    <path d="M0,0 L389,0 C600,45 900,80 1200,84 L1200,540 C1120,548 1060,556 1040,552 L730,577 L71,615 L0,585 Z" fill="var(--orange)"/>
  </svg>
  <nav class="nav"><span>About Us</span><span>Services Provided</span><span>Costs</span><span>Contact Us</span><span>Call to Action</span></nav>
  <div class="abs hero-halo"></div>
  <div class="abs logo-disc"><div class="logo-name">Paw Pals<br>Care</div></div>
  <svg class="abs" style="left:364px;top:36px" width="28" height="28" viewBox="0 0 28 28" aria-hidden="true"><path d="M4,4 L24,12 L9,24 Z" fill="none" stroke="var(--stripe)" stroke-width="3" stroke-linejoin="round"/></svg>
  <svg class="abs" style="left:388px;top:174px" width="22" height="22" viewBox="0 0 22 22" aria-hidden="true"><path d="M3,3 L19,19 M19,3 L3,19" stroke="var(--white)" stroke-width="4" stroke-linecap="round"/></svg>
  <div class="photo hero-dog" role="img" aria-label="Beagle sitting upright, cut out"></div>
  <div class="abs target-mark" role="img" aria-label="Target ring ornament"></div>
  <h1 class="abs hero-title">Your trusted choice for Pet Sitting and Dog Walking</h1>
  <div class="abs wave-mark" role="img" aria-label="Wavy line ornament" style="left:634px;top:444px;width:96px;background:rgba(255,255,255,.55)"></div>

  <!-- about -->
  <div class="abs about-band"></div>
  <div class="abs stripe-disc stripe-warm" role="img" aria-label="Striped circle decoration" style="left:956px;top:448px;width:146px;height:146px"></div>
  <div class="photo about-photo" role="img" aria-label="Person walking two small dogs on leads along a park path"></div>
  <h2 class="abs hand about-title">About us.</h2>
  <p class="abs about-lead">Providing high quality pet care service since 2008</p>
  <p class="abs about-copy">Our professional team of dog walkers are not only your pup’s new best friend, but they’re also a resource you can count on to help manage your busy lifestyle. We specialize in daily dog walking, dog sitting, pet sitting, and training. We also offer an array of other services for both small and large pets. Let us be there for you and your furry family members when you can’t be!</p>

  <!-- services -->
  <h2 class="abs hand services-title">Services.</h2>
  <p class="abs services-sub">Services for all of your pets needs.</p>
  <div class="service" style="left:274px"><div class="service-photo" role="img" aria-label="Golden dog on a lead walking through autumn leaves" style="background:linear-gradient(160deg,#7a6a58,#b67a3e 55%,#8b8276)"></div><p class="service-name">Dog Walking</p></div>
  <div class="service" style="left:508px"><div class="service-photo" role="img" aria-label="Pug resting on a soft blanket" style="background:linear-gradient(160deg,#b8a898,#d9bfa1 55%,#e7e2dc)"></div><p class="service-name">Drop-In Pet Sitting</p></div>
  <div class="service" style="left:739px"><div class="service-photo" role="img" aria-label="Small dog sleeping in a crate with a red blanket" style="background:linear-gradient(160deg,#3a3434,#a8283a 55%,#d9d2cc)"></div><p class="service-name">Overnight Stays</p></div>
  <div class="abs divider" style="width:330px"></div>
  <div class="abs divider" style="left:647px;width:344px"></div>
  <div class="abs wave-mark" role="img" aria-label="Wavy line ornament" style="left:549px;top:1639px;width:90px;background:#c6e0a8"></div>

  <!-- costs -->
  <h2 class="abs hand costs-title">Costs.</h2>
  <p class="abs costs-note">Listed prices are the base rate and may change depending on clients scheduling needs and service add-ons (such as additional pets or holidays).</p>
  <p class="abs hand rate-line">$8 per visit. 2 visits a day.</p>
  <div class="rate-card card-weekday"><h3>Weekday walk</h3><p>Monday-Friday, between<br>9AM And 5PM</p><hr><div class="price"><span>$</span>20</div></div>
  <div class="rate-card card-nights"><h3>Nights &amp; Weekends</h3><p>All visits outside of<br>9AM - 5PM, M-F</p><hr><div class="price"><span>$</span>25</div></div>
  <p class="abs hand rate-foot">we feed, walk and play with your pet, each visit.</p>
  <div class="abs stripe-disc stripe-cool" role="img" aria-label="Striped circle decoration" style="left:895px;top:2071px;width:134px;height:134px"></div>
  <div class="photo retriever" role="img" aria-label="Golden retriever sitting, cut out"></div>

  <!-- contact -->
  <svg class="abs contact-band" width="1200" height="425" viewBox="0 0 1200 425" aria-hidden="true">
    <path d="M434,0 L1200,0 L1200,421 L440,421 C470,380 520,340 500,270 C480,220 400,200 420,140 C440,80 440,40 434,0 Z" fill="var(--yellow)"/>
  </svg>
  <div class="abs stripe-disc stripe-warm" role="img" aria-label="Striped circle decoration" style="left:-40px;top:2306px;width:112px;height:132px"></div>
  <div class="photo contact-art" role="img" aria-label="Illustration of a cartoon dog and cat with paw prints and hearts"></div>
  <h2 class="abs hand contact-title">Contact.</h2>
  <p class="abs contact-hours">Mon - Fri: 7am - 6.30pm<br>Sat - Sun: Closed<br>Bank Holidays: Closed</p>
  <p class="abs contact-address"><strong>Address :</strong>Maple Court,<br>Willow Gardens,<br>Eastfield, Springvale</p>
  <div class="abs stripe-disc stripe-warm" role="img" aria-label="Striped circle decoration" style="left:716px;top:2733px;width:106px;height:106px"></div>
  <div class="photo owner-photo" role="img" aria-label="Woman sitting with two small dogs"></div>
  <div class="photo corgi-photo" role="img" aria-label="Corgi and fluffy dog running outdoors at sunset"></div>

  <!-- conversation -->
  <div class="photo pups-photo" role="img" aria-label="Two happy small dogs on grass"></div>
  <h2 class="abs hand talk-title">Let's start<br>a conversation.</h2>
  <div class="abs wave-mark" role="img" aria-label="Wavy line ornament" style="left:244px;top:2910px;width:96px;background:#f9e7a6"></div>
  <p class="abs talk-copy">We want you to feel confident that your pet is in the best of care. That is why before services begin, Paw Pals Care want you to get to know us and we want to get to know you and your pet family.</p>
  <div class="field" style="left:609px;top:2934px;width:162px">First name</div>
  <div class="field" style="left:793px;top:2934px;width:162px">Last name</div>
  <div class="field" style="left:609px;top:2983px;width:162px">Phone</div>
  <div class="field" style="left:793px;top:2983px;width:162px">Email</div>
  <div class="field" style="left:609px;top:3031px;width:346px;padding-bottom:24px">Message</div>
  <div class="abs submit">Submit yout query</div>

  <!-- footer -->
  <svg class="abs footer-bg" width="1200" height="117" viewBox="0 0 1200 117" aria-hidden="true">
    <path d="M0,42 C200,36 350,16 450,10 L520,26 L900,20 L1000,36 L1200,16 L1200,117 L0,117 Z" fill="var(--orange)"/>
  </svg>
  <p class="abs copyright">Copyright@ 2022 Paw Pals Care. All Right Reserved</p>
</div>
</body>
</html>
```